BQL Groundworks & Freight Business Card

Can you please design a business card for an Earthworks, Haulage truck and machinery hire company. They also provide sand soil and mulch supply, as well as screening of products. Can you re-create the logo from the attached but add BQL Groundworks & Freight just use the three diamond design.

Target Market(s)

Earthmoving and Transport, Landscapers, Construction

Contact Information for Business Card

ABN 52 907 334 816, Doug Pelham, Managing Director, BQL Groundworks & Freight Mobile 0438 256 904 Email bqlfreight2010@mailvane.net

Font styles to use
Sans Serif

Colors
ec1f27
000000
cbcbcb
ffffff

Requirements
Must have
• Listed on the back, Earthworks | Haulage | Truck and Machinery Hire | Sand, Soil & Mulch Supply | Screening of Products
Nice to have
• Would be good for it to look appealing to a mans man, because it relates to heavy machinery, earthworks, construction etc. Black, red and white would be good maybe with a bit of silver somewhere.
Should not have
• not sure

```html
<!DOCTYPE html>
<html lang="en">
<head>
<meta charset="utf-8">
<title>BQL Groundworks &amp; Freight – Business Card</title>
<link rel="stylesheet" href="https://fonts.googleapis.com/css2?family=Lato:wght@400;700;900&family=Tinos:wght@700&display=swap">
<style>
  :root {
    --backdrop: #2a2a2a;
    --card-white: #ffffff;
    --card-silver: #cbcbcb;
    --ink: #000000;
    --accent-red: #ec1f27;
    --card-shadow: rgba(0, 0, 0, 0.6);
  }
  * { margin: 0; padding: 0; box-sizing: border-box; }
  html, body {
    width: 1200px;
    height: 900px;
    overflow: hidden;
    background: var(--backdrop);
  }
  .canvas {
    position: relative;
    width: 1200px;
    height: 900px;
  }
  .card {
    position: absolute;
    left: 330px;
    width: 556px;
    height: 343px;
    background: linear-gradient(160deg, var(--card-white) 0%, #ececec 50%, var(--card-silver) 100%);
    box-shadow: 3px 4px 8px var(--card-shadow);
    color: var(--ink);
    font-family: "Lato", Arial, sans-serif;
    text-align: center;
    overflow: hidden;
  }
  .card--contact { top: 90px; }
  .card--brand { top: 470px; width: 558px; }

  .contact__line {
    position: absolute;
    left: 0;
    width: 100%;
    white-space: nowrap;
    font-size: 15.5px;
    line-height: 1;
  }
  .contact__name {
    top: 62px;
    font-family: "Tinos", "Times New Roman", serif;
    font-weight: 700;
    font-size: 19px;
    letter-spacing: 0.5px;
  }
  .contact__role { top: 83px; }
  .contact__abn { top: 125px; }
  .contact__phone { top: 156px; }
  .contact__email { top: 177px; }
  .contact__street { top: 217px; }
  .contact__city { top: 237px; }
  .contact__tagline { top: 285px; font-size: 15px; }

  .divider {
    position: absolute;
    left: 171px;
    width: 212px;
    height: 1px;
    background: var(--accent-red);
  }
  .divider--1 { top: 111px; }
  .divider--2 { top: 206px; }
  .divider--3 { top: 265px; }

  .brand {
    position: absolute;
    left: 0;
    top: 150px;
    width: 100%;
    display: flex;
    justify-content: center;
    align-items: center;
    gap: 14px;
  }
  .brand__mark {
    width: 30px;
    height: 30px;
    background: var(--accent-red);
  }
  .brand__name {
    font-family: "Lato", Arial, sans-serif;
    font-weight: 900;
    font-size: 29px;
    letter-spacing: 0.5px;
    text-transform: uppercase;
    color: var(--ink);
    white-space: nowrap;
  }
  .brand__rule {
    position: absolute;
    left: 80px;
    top: 205px;
    width: 398px;
    height: 2px;
    background: var(--accent-red);
  }
  .services {
    position: absolute;
    left: 0;
    top: 222px;
    width: 100%;
    font-size: 14px;
    line-height: 22px;
    color: var(--ink);
    white-space: nowrap;
  }
  .services__sep { color: var(--accent-red); padding: 0 6px; }
</style>
</head>
<body>
  <main class="canvas">
    <section class="card card--contact" aria-label="Contact side">
      <p class="contact__line contact__name">DOUG PELHAM</p>
      <p class="contact__line contact__role">Managing Director</p>
      <span class="divider divider--1"></span>
      <p class="contact__line contact__abn">ABN 52 907 334 816</p>
      <p class="contact__line contact__phone">0438 256 904</p>
      <p class="contact__line contact__email">bqlfreight2010@mailvane.net</p>
      <span class="divider divider--2"></span>
      <p class="contact__line contact__street">22 Brambleton Rd Wexcombe 6091</p>
      <p class="contact__line contact__city">Perth,WA</p>
      <span class="divider divider--3"></span>
      <p class="contact__line contact__tagline">FOR ALL YOUR EARTHMOVING AND TRANSPORT NEEDS</p>
    </section>

    <section class="card card--brand" aria-label="Brand side">
      <div class="brand">
        <span class="brand__mark"></span>
        <span class="brand__name">BQL Groundworks &amp; Freight</span>
      </div>
      <span class="brand__rule"></span>
      <div class="services">
        <p>Earthworks<span class="services__sep">|</span>Haulage<span class="services__sep">|</span>Truck and Machinery Hire</p>
        <p>Sand, Soil &amp; Mulch Supply<span class="services__sep">|</span>Screening of Products</p>
      </div>
    </section>
  </main>
</body>
</html>
```